Postcard Design- Market Update - April 2016

Real Estate Agent. I want to be able to enter data into a postcard (see attached) doesn't have to be exact, but similar and with similar info. I did one postcard with this company already - it may help to see the back of it for how i laid it out.

Target Market(s)

Luxury homes - 800,000- 3,000,000

Industry/Entity Type

Real Estate Agent

Requirements
Must have
• Need to be able to edit the 5 data fields. This is for a luxury market...so it can be a little fanicer.

```html
<!DOCTYPE html>
<html lang="en">
<head>
<meta charset="utf-8">
<title>Market Update Postcard</title>
<link rel="stylesheet" href="https://fonts.googleapis.com/css2?family=Arimo:wght@700&family=Open+Sans:wght@600&display=swap">
<style>
  :root {
    --paper: #ffffff;
    --ink: #2b2a29;
    --edge: #2b2a29;
  }
  * { box-sizing: border-box; margin: 0; padding: 0; }
  html, body { width: 1200px; height: 773px; overflow: hidden; background: var(--paper); }
  .postcard {
    position: relative; width: 1200px; height: 773px;
    border: 1px solid var(--edge); display: flex;
  }
  .panel { position: relative; width: 600px; height: 100%; overflow: hidden; }
  .panel--light { background: var(--paper); color: var(--ink); }
  .panel--dark { background: var(--ink); color: var(--paper); }
  .panel__content { position: absolute; inset: 0; }
  .panel--dark .panel__content { transform: translate(13px, 18px); }
  .stat__icon { position: absolute; fill: currentColor; }
  .stat__body { position: absolute; left: 213px; }
  .stat__value {
    font-family: "Arimo", Arial, sans-serif; font-weight: 700;
    font-size: 58px; line-height: 1; letter-spacing: -1px;
  }
  .stat__label {
    font-family: "Open Sans", Arial, sans-serif; font-weight: 600;
    font-size: 21px; line-height: 1.2; margin-top: 9px; white-space: nowrap;
  }
  .digits {
    position: absolute; left: 132px; top: 672px;
    font-family: "Arimo", Arial, sans-serif; font-weight: 700;
    font-size: 62px; line-height: 1; letter-spacing: -1px;
  }
</style>
</head>
<body>
<main class="postcard">
  <section class="panel panel--light">
    <div class="panel__content">
      <svg class="stat__icon" style="left:116px;top:40px" width="62" height="60" viewBox="0 0 62 60" aria-hidden="true">
        <rect x="0" y="26" width="8" height="32" rx="2"/>
        <path d="M11 27 L22 16 C26 11 27 6 28 1 C33 0 36 4 35 11 L33 22 L55 22 C60 22 61 27 58 30 C62 32 61 37 57 38 C60 40 59 45 55 46 C57 48 56 53 52 54 C53 57 51 59 47 59 L11 59 Z"/>
      </svg>
      <div class="stat__body" style="top:38px">
        <div class="stat__value">XX</div>
        <div class="stat__label">Closed Deals</div>
      </div>

      <svg class="stat__icon" style="left:110px;top:154px" width="80" height="69" viewBox="0 0 80 69" aria-hidden="true">
        <path fill-rule="evenodd" d="M8 6 H74 A6 6 0 0 1 80 12 V61 A8 8 0 0 1 72 69 H8 A8 8 0 0 1 0 61 V12 A6 6 0 0 1 6 6 Z
          M5 18 V24 H12 V18 Z M15 18 V24 H22 V18 Z M25 18 V24 H32 V18 Z M35 18 V24 H42 V18 Z M45 18 V24 H52 V18 Z M55 18 V24 H62 V18 Z M65 18 V24 H72 V18 Z
          M5 28 V34 H12 V28 Z M15 28 V34 H22 V28 Z M25 28 V34 H32 V28 Z M35 28 V34 H42 V28 Z M45 28 V34 H52 V28 Z M55 28 V34 H62 V28 Z M65 28 V34 H72 V28 Z
          M5 38 V44 H12 V38 Z M15 38 V44 H22 V38 Z M25 38 V44 H32 V38 Z M35 38 V44 H42 V38 Z M45 38 V44 H52 V38 Z M55 38 V44 H62 V38 Z M65 38 V44 H72 V38 Z
          M5 48 V54 H12 V48 Z M15 48 V54 H22 V48 Z M25 48 V54 H32 V48 Z M35 48 V54 H42 V48 Z M45 48 V54 H52 V48 Z"/>
        <rect x="14" y="0" width="6" height="14" rx="2"/>
        <rect x="60" y="0" width="6" height="14" rx="2"/>
      </svg>
      <div class="stat__body" style="top:159px">
        <div class="stat__value">XX</div>
        <div class="stat__label">Average Days on Market</div>
      </div>

      <svg class="stat__icon" style="left:128px;top:276px" width="44" height="76" viewBox="0 0 44 76" aria-hidden="true">
        <text x="22" y="68" text-anchor="middle" font-family="Arimo, Arial, sans-serif" font-weight="700" font-size="84">$</text>
      </svg>
      <div class="stat__body" style="top:279px">
        <div class="stat__value">XX</div>
        <div class="stat__label">Average Sale Price</div>
      </div>

      <svg class="stat__icon" style="left:110px;top:401px" width="86" height="72" viewBox="0 0 86 72" aria-hidden="true">
        <rect x="0" y="5" width="86" height="3"/>
        <circle cx="22" cy="6.5" r="5"/>
        <circle cx="66" cy="6.5" r="5"/>
        <path fill-rule="evenodd" d="M0 12 H86 V64 A8 8 0 0 1 78 72 H8 A8 8 0 0 1 0 64 Z"/>
        <text x="10" y="36" font-family="Arimo, Arial, sans-serif" font-weight="400" font-size="19" class="sign-text">FOR</text>
        <text x="10" y="63" font-family="Arimo, Arial, sans-serif" font-weight="400" font-size="28" textLength="68" class="sign-text">SALE</text>
      </svg>
      <div class="stat__body" style="top:394px">
        <div class="stat__value">XX</div>
        <div class="stat__label">Homes for Sale</div>
      </div>

      <svg class="stat__icon" style="left:120px;top:527px" width="56" height="67" viewBox="0 0 56 67" aria-hidden="true">
        <path d="M28 0 L55 27 L48 34 L33 19 V63 A4 4 0 0 1 23 63 V19 L8 34 L1 27 Z"/>
      </svg>
      <div class="stat__body" style="top:522px">
        <div class="stat__value">XX%</div>
        <div class="stat__label">Average Home Price</div>
      </div>

      <div class="digits">1234567890</div>
    </div>
  </section>

  <section class="panel panel--dark">
    <div class="panel__content">
      <svg class="stat__icon" style="left:116px;top:40px" width="62" height="60" viewBox="0 0 62 60" aria-hidden="true">
        <rect x="0" y="26" width="8" height="32" rx="2"/>
        <path d="M11 27 L22 16 C26 11 27 6 28 1 C33 0 36 4 35 11 L33 22 L55 22 C60 22 61 27 58 30 C62 32 61 37 57 38 C60 40 59 45 55 46 C57 48 56 53 52 54 C53 57 51 59 47 59 L11 59 Z"/>
      </svg>
      <div class="stat__body" style="top:38px">
        <div class="stat__value">XX</div>
        <div class="stat__label">Closed Deals</div>
      </div>

      <svg class="stat__icon" style="left:110px;top:154px" width="80" height="69" viewBox="0 0 80 69" aria-hidden="true">
        <path fill-rule="evenodd" d="M8 6 H74 A6 6 0 0 1 80 12 V61 A8 8 0 0 1 72 69 H8 A8 8 0 0 1 0 61 V12 A6 6 0 0 1 6 6 Z
          M5 18 V24 H12 V18 Z M15 18 V24 H22 V18 Z M25 18 V24 H32 V18 Z M35 18 V24 H42 V18 Z M45 18 V24 H52 V18 Z M55 18 V24 H62 V18 Z M65 18 V24 H72 V18 Z
          M5 28 V34 H12 V28 Z M15 28 V34 H22 V28 Z M25 28 V34 H32 V28 Z M35 28 V34 H42 V28 Z M45 28 V34 H52 V28 Z M55 28 V34 H62 V28 Z M65 28 V34 H72 V28 Z
          M5 38 V44 H12 V38 Z M15 38 V44 H22 V38 Z M25 38 V44 H32 V38 Z M35 38 V44 H42 V38 Z M45 38 V44 H52 V38 Z M55 38 V44 H62 V38 Z M65 38 V44 H72 V38 Z
          M5 48 V54 H12 V48 Z M15 48 V54 H22 V48 Z M25 48 V54 H32 V48 Z M35 48 V54 H42 V48 Z M45 48 V54 H52 V48 Z"/>
        <rect x="14" y="0" width="6" height="14" rx="2"/>
        <rect x="60" y="0" width="6" height="14" rx="2"/>
      </svg>
      <div class="stat__body" style="top:159px">
        <div class="stat__value">XX</div>
        <div class="stat__label">Average Days on Market</div>
      </div>

      <svg class="stat__icon" style="left:128px;top:276px" width="44" height="76" viewBox="0 0 44 76" aria-hidden="true">
        <text x="22" y="68" text-anchor="middle" font-family="Arimo, Arial, sans-serif" font-weight="700" font-size="84">$</text>
      </svg>
      <div class="stat__body" style="top:279px">
        <div class="stat__value">XX</div>
        <div class="stat__label">Average Sale Price</div>
      </div>

      <svg class="stat__icon" style="left:110px;top:401px" width="86" height="72" viewBox="0 0 86 72" aria-hidden="true">
        <rect x="0" y="5" width="86" height="3"/>
        <circle cx="22" cy="6.5" r="5"/>
        <circle cx="66" cy="6.5" r="5"/>
        <path fill-rule="evenodd" d="M0 12 H86 V64 A8 8 0 0 1 78 72 H8 A8 8 0 0 1 0 64 Z"/>
        <text x="10" y="36" font-family="Arimo, Arial, sans-serif" font-weight="400" font-size="19" class="sign-text">FOR</text>
        <text x="10" y="63" font-family="Arimo, Arial, sans-serif" font-weight="400" font-size="28" textLength="68" class="sign-text">SALE</text>
      </svg>
      <div class="stat__body" style="top:394px">
        <div class="stat__value">XX</div>
        <div class="stat__label">Homes for Sale</div>
      </div>

      <svg class="stat__icon" style="left:120px;top:527px" width="56" height="67" viewBox="0 0 56 67" aria-hidden="true">
        <path d="M28 0 L55 27 L48 34 L33 19 V63 A4 4 0 0 1 23 63 V19 L8 34 L1 27 Z"/>
      </svg>
      <div class="stat__body" style="top:522px">
        <div class="stat__value">XX%</div>
        <div class="stat__label">Average Home Price</div>
      </div>

      <div class="digits">1234567890</div>
    </div>
  </section>
</main>
<style>
  .panel--light .sign-text { fill: var(--paper); }
  .panel--dark .sign-text { fill: var(--ink); }
</style>
</body>
</html>
```